Tea box package for Herbal Teas

We would like a design for a package of our tea products. We want the consumer to understand that our products are natural just by looking at the package. We prefer minimalistic designs.
The package we want would be a square (or slightly rectangular) box. The box would be generic enough for us to use it for different teas. Essentially what we want is all the main information and designs to be the same for each tea product we have. We would like to be able to change the main color and the name of the tea then to customize to the tea in the package. Please see the attached images for examples.
We really like the package in tea_packaging_example_4 picture. We would like our packaging to be something very similar but with all the labels printed on the package.
We already have our logo so I am attaching that as well (image named 'velk ansary logo copy'). That would go on the front of the box.
We also attach a tile created using our logo (see image called 'tile'). We would like this to go to the sides similarly to tea_packaging_example_4.
On the back of the pouch, we want to have directions on how to make the tea but we want this section to be editable. For now just 3-4 lines of sample text is fine along with instructions on how to make a tea, see picture 'back of tea box'.
We would like for the box color to be as in example picture
tea_packaging_example_4. The color of the writing should be the same as the logo color. The font style should be something that would look nice next to the logo font, we are not sure what that font should be. The only thing colored would be the name of the tea and the ribbon as seen in tea_packaging_example_4, which we would like to change if we need to, to other variations.
Thanks a lot. For any questions, please contact me.

```html
<!DOCTYPE html>
<html lang="en">
<head>
<meta charset="utf-8">
<title>Velk Ansary – Cool Mint Herb Infusion box dieline</title>
<link rel="stylesheet" href="https://fonts.googleapis.com/css2?family=Jost:wght@400;500;600&display=swap">
<style>
  :root {
    --backdrop: #d7d9d8;
    --paper: #f4f4f2;
    --cut-line: #3a3a3a;
    --fold-line: #9a9a9a;
    --ink: #1e1e1e;
    --ribbon: #1b9848;
    --ribbon-edge: #1a1a1a;
    --tile: #38b04b;
    --label-white: #ffffff;
  }
  html, body {
    margin: 0;
    padding: 0;
    width: 1173px;
    height: 1200px;
    overflow: hidden;
    background: var(--backdrop);
  }
  .dieline {
    position: absolute;
    left: 0;
    top: 167px;
    width: 1173px;
    height: 866px;
    font-family: "Jost", sans-serif;
  }
  .cut { fill: var(--paper); stroke: var(--cut-line); stroke-width: 1.6; }
  .fold { stroke: var(--fold-line); stroke-width: 1; stroke-dasharray: 3 3; fill: none; }
  .side-tile { fill: var(--tile); }
  .ribbon { fill: var(--ribbon); }
  .ribbon-rule { stroke: var(--ribbon-edge); stroke-width: 3; }
  .brand-dot { fill: none; stroke: var(--ink); stroke-width: 2.5; }
  .brand-name { fill: var(--ink); font-weight: 500; letter-spacing: 0.06em; }
  .tea-name { fill: var(--label-white); font-weight: 500; letter-spacing: 0.02em; }
  .tea-type { fill: var(--label-white); font-weight: 400; letter-spacing: 0.06em; }
  .net-weight { fill: var(--ink); font-size: 11px; }
  .back-copy { fill: var(--ink); font-size: 8.6px; }
  .back-copy .lead { font-weight: 600; }
  .web { fill: var(--ink); font-size: 7.5px; font-weight: 600; }
</style>
</head>
<body>
<svg class="dieline" viewBox="110 545 1240 915" xmlns="http://www.w3.org/2000/svg">
  <!-- box outline -->
  <path class="cut" d="
    M180,920 L135,928 Q125,930 125,940 L125,1180 Q125,1190 135,1192 L180,1200
    L180,1362 L320,1362 L320,1300 L338,1292 L465,1205
    L465,1445 L535,1445 L535,1340 L680,1340 L680,1445 L750,1445 L750,1205
    L890,1290 L868,1300 L868,1362 L1035,1362
    L1120,1362 L1120,1445 L1250,1445 L1250,1362 L1320,1362
    L1320,635 L1316,580 Q1310,565 1290,565 L1065,565 Q1045,565 1040,580 L1035,635
    L1035,790 Q1035,775 1020,775 L765,775 Q750,775 750,790 L750,920
    L465,920 L465,790 Q465,775 450,775 L195,775 Q180,775 180,790 Z"/>

  <!-- fold lines -->
  <line class="fold" x1="180" y1="920" x2="1320" y2="920"/>
  <line class="fold" x1="180" y1="1205" x2="1320" y2="1205"/>
  <line class="fold" x1="1035" y1="635" x2="1320" y2="635"/>
  <line class="fold" x1="465" y1="920" x2="465" y2="1205"/>
  <line class="fold" x1="750" y1="920" x2="750" y2="1205"/>
  <line class="fold" x1="1035" y1="920" x2="1035" y2="1362"/>

  <!-- side panels: brand tile pattern -->
  <rect class="side-tile" x="180" y="922" width="285" height="278" role="img" aria-label="Green repeating brand tile pattern on the left side panel"/>
  <rect class="side-tile" x="750" y="922" width="285" height="278" role="img" aria-label="Green repeating brand tile pattern on the right side panel"/>

  <!-- front panel -->
  <g class="front-panel">
    <circle class="brand-dot" cx="607" cy="985" r="20"/>
    <text class="brand-name" x="607" y="1041" font-size="14" text-anchor="middle">VELK ANSARY</text>
    <rect class="ribbon" x="465" y="1075" width="285" height="86"/>
    <line class="ribbon-rule" x1="465" y1="1074" x2="750" y2="1074"/>
    <line class="ribbon-rule" x1="465" y1="1162" x2="750" y2="1162"/>
    <text class="tea-name" x="607" y="1121" font-size="38" text-anchor="middle">COOL MINT</text>
    <text class="tea-type" x="607" y="1146" font-size="14" text-anchor="middle">• HERB INFUSION •</text>
    <text class="net-weight" x="607" y="1185" text-anchor="middle">Net Wt 37.5g 13 OZ</text>
  </g>

  <!-- lid (printed upside down) -->
  <g class="lid" transform="rotate(180 1178 750)">
    <circle class="brand-dot" cx="1178" cy="710" r="32"/>
    <text class="brand-name" x="1178" y="800" font-size="24" text-anchor="middle">VELK ANSARY</text>
  </g>

  <!-- back panel -->
  <g class="back-panel">
    <circle class="brand-dot" cx="1178" cy="962" r="13"/>
    <text class="brand-name" x="1178" y="999" font-size="9" text-anchor="middle">VELK ANSARY</text>
    <text class="back-copy" text-anchor="middle">
      <tspan class="lead" x="1178" y="1018">Lorem ipsum dolor sit amet.</tspan>
      <tspan x="1178" y="1029">Consectetuer adipiscing elit, sed diam nonummy nibh euismod</tspan>
      <tspan x="1178" y="1040">tincidunt ut laoreet dolore magna aliquam erat volutpat.</tspan>
      <tspan x="1178" y="1058"><tspan class="lead">Ut wisi enim:</tspan> ad minim veniam, quis nostrud exerci tation</tspan>
      <tspan x="1178" y="1069">ullamcorper suscipit lobortis nisl ut aliquip ex ea commodo</tspan>
      <tspan x="1178" y="1080">consequat.</tspan>
      <tspan x="1178" y="1098"><tspan class="lead">Duis autem:</tspan> vel eum iriure dolor in hendrerit in vulputate velit</tspan>
      <tspan x="1178" y="1109">esse molestie consequat, vel illum dolore eu feugiat nulla</tspan>
      <tspan x="1178" y="1120">facilisis at vero eros et accumsan et iusto odio dignissim qui</tspan>
      <tspan x="1178" y="1131">blandit praesent luptatum zzril delenit augue duis dolore te</tspan>
      <tspan x="1178" y="1142">feugait nulla facilisi.</tspan>
    </text>
    <text class="web" x="1178" y="1162" text-anchor="middle">www.velkansary.com</text>
  </g>
</svg>
</body>
</html>
```